Ginger Beer Can Design for a none alcoholic bavarage

We need a cool, modern, fresh design for a can.

- 330ml sleek can size
- 0.0% alcohol
- BIO
- ingredience: Water, Sugar, Ginger, limejuice, Gummi Arabicum, Carbonisation
- Energy table of fats, carbs, protein, etc.
- address: Quiet Meadow Drinks, Lindenweg 42, 4052 Basel

```html
<!DOCTYPE html>
<html lang="en">
<head>
<meta charset="utf-8">
<title>Ginger &amp; Lime Sparkling Infusion – Can Label</title>
<link rel="stylesheet" href="https://fonts.googleapis.com/css2?family=Alfa+Slab+One&family=Montserrat:wght@500;600;700;800&display=swap">
<style>
  :root {
    --stage: #b8e04c;
    --label-dark: #121412;
    --label-olive: #3a4a12;
    --lime: #b5dd3f;
    --leaf-green: #4fb443;
    --deep-green: #1f5a24;
    --yellow: #ffe81a;
    --white: #ffffff;
    --ink: #111111;
  }
  * { margin: 0; padding: 0; box-sizing: border-box; }
  html, body { width: 1200px; height: 2456px; overflow: hidden; }
  body {
    background: var(--stage);
    font-family: "Montserrat", sans-serif;
    position: relative;
  }
  .label {
    position: absolute;
    left: 89px;
    top: 835px;
    width: 1022px;
    height: 785px;
    overflow: hidden;
    background: radial-gradient(ellipse at 0% 0%, var(--label-olive) 0%, #1b2014 40%, var(--label-dark) 70%);
    box-shadow: 0 10px 30px rgba(0,0,0,0.25);
  }
  .label-art { position: absolute; inset: 0; }
  .brand {
    position: absolute;
    left: 193px; top: 70px;
    width: 200px;
    text-align: center;
    color: var(--white);
    font-weight: 800;
    font-size: 26px;
    line-height: 1.15;
    letter-spacing: 1px;
  }
  .brand-dot {
    display: block;
    width: 40px; height: 40px;
    border-radius: 50%;
    background: var(--white);
    margin: 0 auto 14px;
  }
  .product-name {
    position: absolute;
    left: 140px; top: 305px;
    width: 320px;
    color: var(--white);
    font-family: "Alfa Slab One", serif;
    font-weight: 400;
    font-size: 60px;
    line-height: 60px;
    text-align: center;
    transform: skewX(-8deg);
  }
  .pill {
    position: absolute;
    background: var(--yellow);
    color: var(--ink);
    font-weight: 700;
    border-radius: 4px;
    white-space: nowrap;
  }
  .subtitle { left: 167px; top: 429px; width: 252px; height: 33px; font-size: 19px; text-align: center; line-height: 33px; font-weight: 600; }
  .brush {
    position: absolute;
    left: 83px; top: 477px;
    width: 430px; height: 295px;
    background: linear-gradient(160deg, #6acb4a 0%, var(--leaf-green) 50%, #2e8a2c 100%);
    clip-path: polygon(18% 8%, 100% 0%, 86% 30%, 92% 58%, 76% 84%, 68% 100%, 28% 100%, 0% 88%, 6% 50%);
  }
  .fruit {
    position: absolute;
    left: 170px; top: 520px;
    width: 230px; height: 170px;
    border-radius: 50%;
    background: radial-gradient(circle at 55% 50%, #f7dd5c 0%, #e6bf3c 45%, rgba(200,150,80,0.6) 75%, rgba(79,180,67,0) 100%);
  }
  .alcohol {
    position: absolute;
    left: 305px; top: 510px;
    width: 145px; height: 29px;
    background: var(--white);
    color: var(--ink);
    border-radius: 15px;
    font-size: 16px; font-weight: 600;
    text-align: center; line-height: 29px;
  }
  .organic {
    position: absolute;
    left: 118px; top: 630px;
    color: var(--white);
    font-size: 14px; font-weight: 700;
    line-height: 12px;
  }
  .organic small { font-size: 10px; display: block; }
  .volume {
    position: absolute;
    left: 255px; top: 730px;
    width: 100px;
    text-align: center;
    color: var(--ink);
    font-size: 17px; font-weight: 600;
    line-height: 22px;
  }
  .section-tag { height: 31px; line-height: 31px; font-size: 18px; padding: 0 13px; }
  .tag-ingredients { left: 542px; top: 57px; }
  .tag-maker { left: 542px; top: 640px; }
  .ingredients {
    position: absolute;
    left: 556px; top: 110px;
    width: 320px;
    color: var(--white);
    font-size: 19px; font-weight: 600;
    line-height: 23px;
  }
  .nutrition {
    position: absolute;
    left: 542px; top: 245px;
    width: 372px;
    border-collapse: collapse;
    color: var(--white);
    font-size: 19px; font-weight: 600;
  }
  .nutrition th {
    background: var(--yellow);
    color: var(--ink);
    font-weight: 800;
    height: 45px;
    text-align: left;
    padding-left: 14px;
    font-size: 18px;
    border: 1px solid var(--yellow);
  }
  .nutrition th.value-col { text-align: center; padding-left: 0; }
  .nutrition td {
    height: 43px;
    padding-left: 14px;
    border: 1.5px solid #cfd3cf;
  }
  .nutrition td.value { text-align: center; padding-left: 0; width: 141px; }
  .maker {
    position: absolute;
    left: 556px; top: 690px;
    color: var(--white);
    font-size: 19px; font-weight: 700;
    line-height: 23px;
  }
</style>
</head>
<body>
  <div class="label">
    <svg class="label-art" width="1022" height="785" viewBox="0 0 1022 785">
      <defs>
        <linearGradient id="curveGreen" x1="0" y1="0" x2="0" y2="1">
          <stop offset="0" stop-color="#d3ec4a"/>
          <stop offset="0.5" stop-color="#a7d53d"/>
          <stop offset="1" stop-color="#5fbd45"/>
        </linearGradient>
      </defs>
      <path class="side-band" d="M769,0 C960,130 1015,500 760,785 L1022,785 L1022,0 Z" fill="url(#curveGreen)"/>
      <g role="img" aria-label="Dark lime slice illustration">
        <circle cx="1030" cy="55" r="90" fill="#151815"/>
      </g>
      <g role="img" aria-label="Dark leaf ornament">
        <ellipse cx="985" cy="735" rx="28" ry="50" fill="#151815" transform="rotate(35 985 735)"/>
      </g>
      <g role="img" aria-label="Faint green leaves ornament">
        <ellipse cx="740" cy="605" rx="120" ry="32" fill="#1d4a1f" opacity="0.8"/>
      </g>
    </svg>

    <div class="brand"><span class="brand-dot"></span>QUIET MEADOW DRINKS</div>

    <h1 class="product-name">GINGER<br>&amp; LIME</h1>
    <div class="pill subtitle">SPARKLING INFUSION</div>

    <div class="brush" role="img" aria-label="Green brush stroke backdrop"></div>
    <div class="fruit" role="img" aria-label="Lemons, lime slice, leaves and ginger root"></div>
    <div class="alcohol">0.0% Alcohol</div>
    <div class="organic">100%<small>ORGANIC</small></div>
    <div class="volume">330ml</div>

    <div class="pill section-tag tag-ingredients">INGREDIENCE:</div>
    <p class="ingredients">Water, Sugar, Ginger, limejuice, Gummi Arabicum, Carbonisation.</p>

    <table class="nutrition">
      <thead>
        <tr><th>NUTRITIONAL DATA</th><th class="value-col">PER 100ML</th></tr>
      </thead>
      <tbody>
        <tr><td>Energy</td><td class="value">00</td></tr>
        <tr><td>Fat</td><td class="value">00</td></tr>
        <tr><td>Carbohydrates</td><td class="value">00</td></tr>
        <tr><td>Protein</td><td class="value">00</td></tr>
        <tr><td>Salt</td><td class="value">00</td></tr>
      </tbody>
    </table>

    <div class="pill section-tag tag-maker">MANUFACTURED BY:</div>
    <p class="maker">QUIET MEADOW DRINKS<br>Lindenweg 42, 4052 Basel</p>
  </div>
</body>
</html>
```